winelabels - new design - redesign the existing winelabels

we want to redesign our winelabels, but we want to keep the basic idea of the labels. we want to have a connection to the new label (see sample). Only the basic information should be on the main label, all other informations should be on the side, like in the new label.
restrictions - not wider than 12 cm, the high is fexibel.
we have about 12 different pictures we use for our labels. They have two different highst (see samples). we have two different types of bottles. If you need more information, please give response.
May have a look to our homepage and our shop under www.falkenried-obermaier.de

Reason: there are a lot of very good ideas, but we are still looking for the "perfect" idea

Font styles to use
Other font styles liked:
• for the name "falkenried-obermaier" use the font simelar to the design " Riesling or Muscaris" everthing else is open

Requirements
Must have
• a connection between old an new design

```html
<!DOCTYPE html>
<html lang="de">
<head>
<meta charset="utf-8">
<title>Falkenried-Obermaier – Weinetiketten</title>
<link rel="stylesheet" href="https://fonts.googleapis.com/css2?family=Cinzel:wght@400&family=Cormorant+Garamond:ital,wght@0,400;0,500;1,400&family=EB+Garamond:wght@400&display=swap">
<style>
  :root {
    --backdrop: #d4d4d4;
    --label-cream: #efe5c9;
    --label-cream-edge: #e4d7b4;
    --ink-brown: #5a3518;
    --rule-brown: #4a2a10;
    --art-boy-a: #8a7f86;
    --art-boy-b: #4f6790;
    --art-boy-c: #a4856f;
    --art-flower-a: #c9c2c4;
    --art-flower-b: #c8463a;
    --art-flower-c: #8fa39a;
  }
  * { box-sizing: border-box; margin: 0; padding: 0; }
  html, body { width: 1200px; height: 800px; overflow: hidden; }
  body {
    background: radial-gradient(ellipse at 50% 40%, #e6e6e6 0%, var(--backdrop) 70%);
    position: relative;
    font-family: "EB Garamond", serif;
  }
  .label {
    position: absolute;
    top: 235px;
    width: 500px;
    height: 330px;
    background: linear-gradient(180deg, var(--label-cream) 0%, var(--label-cream-edge) 100%);
    display: flex;
    box-shadow: 0 6px 22px rgba(0,0,0,0.12);
  }
  .label--benavira { left: 60px; }
  .label--pinotin { left: 640px; }
  .label__art { width: 92px; height: 100%; flex: none; }
  .label__art--portrait {
    background: linear-gradient(160deg, var(--art-boy-a) 0%, var(--art-boy-b) 45%, var(--art-boy-c) 100%);
  }
  .label__art--flowers {
    background: radial-gradient(circle at 55% 40%, var(--art-flower-b) 0%, #a8443d 22%, var(--art-flower-c) 50%, var(--art-flower-a) 85%);
  }
  .label__rule {
    width: 5px; flex: none;
    margin-left: 8px;
    background: var(--rule-brown);
  }
  .label__main {
    flex: 1;
    display: flex;
    flex-direction: column;
    align-items: center;
    padding-top: 34px;
    color: var(--ink-brown);
  }
  .winery {
    display: flex;
    flex-direction: column;
    align-items: center;
    gap: 10px;
  }
  .winery__dot {
    width: 30px; height: 30px;
    border-radius: 50%;
    background: var(--ink-brown);
  }
  .winery__name {
    font-family: "Cormorant Garamond", serif;
    font-weight: 500;
    font-size: 23px;
    letter-spacing: 0.3px;
    color: var(--ink-brown);
  }
  .wine__name {
    margin-top: 62px;
    font-family: "Cinzel", serif;
    font-size: 30px;
    letter-spacing: 2px;
  }
  .wine__vintage {
    margin-top: 10px;
    font-family: "EB Garamond", serif;
    font-size: 18px;
  }
  .wine__style {
    margin-top: 58px;
    font-family: "EB Garamond", serif;
    font-size: 17px;
    letter-spacing: 1px;
  }
  .label__side {
    width: 46px; flex: none;
    padding: 14px 6px;
    writing-mode: vertical-rl;
    font-family: "EB Garamond", serif;
    font-size: 7.5px;
    line-height: 11px;
    color: var(--ink-brown);
  }
</style>
</head>
<body>
  <section class="label label--benavira">
    <div class="label__art label__art--portrait" role="img" aria-label="Gemälde: Bildnis eines Jungen in blauer Jacke"></div>
    <div class="label__rule"></div>
    <div class="label__main">
      <div class="winery">
        <span class="winery__dot"></span>
        <span class="winery__name">Falkenried-Obermaier</span>
      </div>
      <h1 class="wine__name">Benavira</h1>
      <p class="wine__vintage">2015</p>
      <p class="wine__style">TROCKEN</p>
    </div>
    <div class="label__side">
      <p>2015 · Qualitätswein · im Holzfass gereift · eine neue Rebsorte aus</p>
      <p>dem Burgund, fruchtig und kräftig mit feiner Würze</p>
      <p>Pilzwiderstandsfähige Rebsorte, enthält Sulfite, Gutsabfüllung</p>
    </div>
  </section>

  <section class="label label--pinotin">
    <div class="label__art label__art--flowers" role="img" aria-label="Gemälde: rote Blumen in einer Glasvase"></div>
    <div class="label__rule"></div>
    <div class="label__main">
      <div class="winery">
        <span class="winery__dot"></span>
        <span class="winery__name">Falkenried-Obermaier</span>
      </div>
      <h1 class="wine__name">Pinotin</h1>
      <p class="wine__vintage">2015</p>
      <p class="wine__style">TROCKEN</p>
    </div>
    <div class="label__side">
      <p>2015 · Qualitätswein · im Holzfass gereift · eine neue Rebsorte aus</p>
      <p>dem Burgund, fruchtig und kräftig mit feiner Würze</p>
      <p>Pilzwiderstandsfähige Rebsorte, enthält Sulfite, Gutsabfüllung</p>
    </div>
  </section>
</body>
</html>
```